HUSH: Hush Until Stories Happen school library event

I need two poster designs for Hush Until Stories Happen (HUSH) in BC, requested by the PCSMG--Pacific Coast School Media Guild. One should be for elementary students and one for high school. I want the date (Monday, October 26, 2020) and Hush Until Stories Happen. I would like the posters in English and in French. French is : Ferme Ton Écran Maintenant! I'm including last year's posters as examples. I would like to be able to print the poster files on 11x17 paper.

• -The phrase "Hush Until Stories Happen" for the English version; "Ferme Ton Écran Maintenant" for the French version.
-Include the organization name: Pacific Coast School Media Guild
-The date: Monday, October 26, 2020
• I would like the elementary version to be bright and colourful--fun for younger kids. I would like the high school version to be a bit more mature for the older students. Can still be bright and colourful.

```html
<!DOCTYPE html>
<html lang="en">
<head>
<meta charset="utf-8">
<title>HUSH – Hush Until Stories Happen</title>
<link rel="stylesheet" href="https://fonts.googleapis.com/css2?family=Jost:wght@400;700;800;900&display=swap">
<style>
  :root {
    --paper: #ffffff;
    --sky-top: #6c9ddd;
    --sky-mid: #3d7cc9;
    --sky-bottom: #2565b4;
    --headline: #dde4f3;
    --ink: #0b0b0f;
    --date: #ffffff;
    --photo-a: #4f87cf;
    --photo-b: #2b4f7e;
    --photo-c: #8a5a34;
  }
  html, body {
    margin: 0;
    padding: 0;
    overflow: hidden;
    background: var(--paper);
  }
  .poster {
    position: relative;
    width: 777px;
    height: 1200px;
    background: var(--paper);
    overflow: hidden;
    font-family: "Jost", "Futura", sans-serif;
  }
  .poster__field {
    position: absolute;
    left: 17px;
    top: 17px;
    width: 736px;
    height: 1155px;
    background: radial-gradient(ellipse at 55% 30%, var(--sky-top) 0%, var(--sky-mid) 55%, var(--sky-bottom) 100%);
    overflow: hidden;
  }
  .poster__photo {
    position: absolute;
    left: 0;
    top: 50px;
    width: 285px;
    height: 1105px;
    background: linear-gradient(180deg, var(--photo-a) 0%, var(--photo-b) 35%, var(--photo-b) 60%, var(--photo-c) 80%, var(--photo-a) 100%);
    opacity: 0.85;
  }
  .poster__text {
    position: absolute;
    left: 231px;
    top: 0;
    width: 500px;
  }
  .org-name {
    position: absolute;
    top: 66px;
    left: 0;
    margin: 0;
    font-weight: 400;
    font-size: 23px;
    line-height: 29px;
    letter-spacing: 0.3px;
    color: var(--ink);
    text-transform: uppercase;
  }
  .presents {
    position: absolute;
    top: 166px;
    left: 0;
    margin: 0;
    font-weight: 900;
    font-size: 36px;
    line-height: 1;
    color: var(--ink);
  }
  .headline {
    position: absolute;
    top: 204px;
    left: 0;
    margin: 0;
    font-weight: 900;
    color: var(--headline);
    text-transform: uppercase;
    white-space: nowrap;
    text-shadow: 6px 9px 12px rgba(8, 30, 80, 0.35);
  }
  .headline__line {
    display: block;
    font-size: 78px;
    line-height: 79px;
    letter-spacing: -0.5px;
  }
  .headline__line--big {
    font-size: 108px;
    line-height: 144px;
    letter-spacing: -2px;
  }
  .event-date {
    position: absolute;
    top: 1068px;
    left: 0;
    margin: 0;
    font-weight: 700;
    font-size: 32px;
    letter-spacing: 0.6px;
    color: var(--date);
    white-space: nowrap;
  }
</style>
</head>
<body>
  <main class="poster">
    <div class="poster__field">
      <div class="poster__photo" role="img" aria-label="Photo of a young child in a red knit hat, striped shirt and denim overalls sitting on a wooden stool reading a small book"></div>
      <div class="poster__text">
        <p class="org-name">Pacific Coast<br>School Media<br>Guild</p>
        <p class="presents">PRESENTS</p>
        <h1 class="headline">
          <span class="headline__line">Hush</span>
          <span class="headline__line">Until</span>
          <span class="headline__line">Stories</span>
          <span class="headline__line headline__line--big">Happen</span>
        </h1>
        <p class="event-date">MONDAY, OCTOBER 26, 2020</p>
      </div>
    </div>
  </main>
</body>
</html>
```